Stationery Design Project

Please use logo on top corner and place a watermark of the logo on center of the page. Also please add address on bottom as a watermark type of font/colour.

Target Market(s)

FInancial profesionals and high net work individuals

Font styles to use
Serif
Sans Serif

```html
<!DOCTYPE html>
<html lang="en">
<head>
<meta charset="utf-8">
<title>Recommendation – Harwell Equity Finance</title>
<link rel="stylesheet" href="https://fonts.googleapis.com/css2?family=Arimo&family=Cormorant+Garamond:wght@500&display=swap">
<style>
  :root {
    --paper: #ffffff;
    --ink: #1a1a1a;
    --brand-navy: #23317a;
    --watermark: #e3e3e3;
    --address-grey: #6b6b6b;
  }
  html, body {
    margin: 0;
    padding: 0;
    overflow: hidden;
    background: var(--paper);
  }
  .letterhead {
    position: relative;
    width: 848px;
    height: 1200px;
    overflow: hidden;
    background: var(--paper);
  }
  .brand {
    position: absolute;
    top: 34px;
    left: 0;
    width: 100%;
    display: flex;
    flex-direction: column;
    align-items: center;
    gap: 10px;
  }
  .brand-dot {
    width: 44px;
    height: 44px;
    border-radius: 50%;
    background: var(--brand-navy);
  }
  .brand-name {
    font-family: "Cormorant Garamond", serif;
    font-weight: 500;
    font-size: 17px;
    letter-spacing: 1px;
    color: var(--brand-navy);
    margin: 0;
  }
  .page-watermark {
    position: absolute;
    left: 160px;
    top: 330px;
    width: 560px;
    height: 560px;
  }
  .doc-title {
    position: absolute;
    top: 244px;
    left: 0;
    width: 100%;
    margin: 0;
    text-align: center;
    font-family: "Cormorant Garamond", serif;
    font-weight: 500;
    font-size: 23px;
    letter-spacing: 3.5px;
    color: var(--ink);
  }
  .letter-body {
    position: absolute;
    top: 302px;
    left: 105px;
    width: 642px;
    font-family: "Arimo", sans-serif;
    font-size: 16px;
    line-height: 19px;
    color: var(--ink);
  }
  .letter-body p {
    margin: 0 0 19px;
    text-indent: 55px;
  }
  .letter-body .salutation {
    text-indent: 0;
    margin-bottom: 19px;
  }
  .address {
    position: absolute;
    right: 100px;
    top: 1097px;
    margin: 0;
    text-align: right;
    font-family: "Cormorant Garamond", serif;
    font-style: normal;
    font-size: 19px;
    line-height: 25px;
    letter-spacing: 1.2px;
    color: var(--address-grey);
  }
</style>
</head>
<body>
<main class="letterhead">
  <header class="brand">
    <span class="brand-dot" aria-hidden="true"></span>
    <p class="brand-name">Harwell Equity Finance</p>
  </header>

  <svg class="page-watermark" viewBox="0 0 560 560" role="img" aria-label="Faint company emblem watermark">
    <circle cx="280" cy="280" r="270" fill="var(--watermark)" opacity="0.6"/>
  </svg>

  <h1 class="doc-title">RECOMMENDATION</h1>

  <section class="letter-body">
    <p class="salutation">To Whom It May Concern:</p>
    <p>It is my sincere pleasure to write this Letter of Recommendation on behalf of Jordan L. Reeve, a former direct report of mine.</p>
    <p>Jordan exemplifies sustained superior performance. When given the most challenging assignments, you can expect results far above many more experienced employees.</p>
    <p>Expectations only need to be communicated once with this remarkable person. Always one to lead by example, Jordan is well-respected by peers and superiors alike. Whether working individually or in teams, the result is outstanding every time.</p>
    <p>I recall a particularly tough quarter for our company. We had some short deadlines, several mission-critical projects to complete, and a few new employees with little to no experience. Jordan put a plan into action that played to the strengths of our inexperienced teammates. The results were phenomenal – we met our objectives on time and under budget!</p>
    <p>I hate to lose Jordan, but there comes a time in everyone’s life where opportunity and preparedness meet. This is that time for Jordan Reeve!</p>
    <p>Feel free to call me directly to discuss Jordan in more detail. Hire Jordan L. Reeve and you hire a winner!</p>
    <p>Sincerely,</p>
  </section>

  <address class="address">412 E. Elm St.<br>Hartford, KS 67854</address>
</main>
</body>
</html>
```